Business Card Design Project

We need a business card design for a new company based in New York called "Kestrel Co's". We do major installations of energy saving devices primarily LED lighting in large facilities. We would like a double sided card with our contact info on one side with our logo (to be designed) and on the other side the services we provide. We would like a heavy weight glossy card using the colors green and white. The final design should communicate environmental soundness and our market is very upscale corporations.
We would like our logo to illustrate LED lighting and we were thinking if we could get a stock picture of the Calloway Spire Tower lit up on July 4th with red, white and blue LED lighting. The alternative would be anything that connotes environmentally proper thinking. It could be either a picture or a design.

```html
<!DOCTYPE html>
<html lang="en">
<head>
<meta charset="utf-8">
<title>Kestrel Co's – Business Card</title>
<link href="https://fonts.googleapis.com/css2?family=Questrial&display=swap" rel="stylesheet">
<style>
  :root {
    --page-bg: #ecefea;
    --card-white: #ffffff;
    --brand-green: #0f7a3a;
    --green-light: #8dc63f;
    --green-dark: #066b35;
    --ink: #111111;
    --shadow: rgba(0, 0, 0, 0.18);
  }
  * { box-sizing: border-box; margin: 0; padding: 0; }
  html, body {
    width: 1200px;
    height: 1000px;
    overflow: hidden;
    background: var(--page-bg);
    font-family: "Questrial", "Century Gothic", sans-serif;
  }
  .canvas {
    position: relative;
    width: 1200px;
    height: 1000px;
  }
  .card {
    position: absolute;
    box-shadow: 0 10px 30px var(--shadow);
    overflow: hidden;
  }

  /* Back: contact side */
  .card-back {
    left: 90px;
    top: 340px;
    width: 600px;
    height: 343px;
    background: var(--card-white);
  }
  .services {
    position: absolute;
    top: 16px;
    left: 30px;
    right: 20px;
    color: var(--brand-green);
    font-size: 21px;
    font-style: italic;
    letter-spacing: 0.3px;
    white-space: nowrap;
  }
  .contact {
    position: absolute;
    left: 44px;
    top: 120px;
    color: var(--ink);
    font-size: 14px;
    font-style: italic;
    line-height: 1.3;
  }
  .contact .identity { text-transform: uppercase; }
  .contact .lines { margin-top: 18px; }
  .back-name {
    position: absolute;
    right: 10px;
    top: 60px;
    height: 270px;
    writing-mode: vertical-rl;
    color: var(--brand-green);
    font-size: 40px;
    letter-spacing: 4px;
    text-align: end;
    line-height: 1;
  }

  /* Front: brand side */
  .card-front {
    left: 760px;
    top: 200px;
    width: 343px;
    height: 600px;
    background: linear-gradient(160deg, var(--green-light) 0%, #3a9a3c 45%, var(--green-dark) 100%);
  }
  .front-name {
    position: absolute;
    left: 50%;
    top: 50%;
    transform: translate(-50%, -50%);
    writing-mode: vertical-rl;
    color: var(--card-white);
    font-size: 96px;
    letter-spacing: 8px;
    white-space: nowrap;
    line-height: 1;
  }
</style>
</head>
<body>
<main class="canvas">
  <section class="card card-back" aria-label="Card back with contact details">
    <p class="services">lighting . LED . decorating . home . office . parties</p>
    <div class="contact">
      <p class="identity">Name</p>
      <p class="identity">Occupation</p>
      <p>234a Kestrel Street</p>
      <p>Location, State, ZipCode, Country</p>
      <div class="lines">
        <p>Ph: 555 55555</p>
        <p>E: hello@kestrelcos.com</p>
        <p>W: www.kestrelcos.com</p>
      </div>
    </div>
    <p class="back-name">Kestrel Co's</p>
  </section>

  <section class="card card-front" aria-label="Card front with company name">
    <p class="front-name">Kestrel Co's</p>
  </section>
</main>
</body>
</html>
```